Business Card for new Architectural Firm

I intend to practice in a rural mountain community in upstate NY, focusing on residential and light commercial projects, including second home / vacation properties. I wish to convey a feeling of rural outdoorsy modernity.

Color is important - bold and urbane. Secondary or tertiary colors preferred.

Font is important, idiosyncratic is ok

Optionally, I may choose to use the name Brackenfold Studio. If used as part of your design, all of the Must Haves are still required.

Images uploaded are logos I like

Industry/Entity Type

Residential

Contact Information for Business Card

Caldwell Prusinski
Architect (This word should stand alone or be associated with my name - not license number)
NY License No. 582163
caldwell@designcpx.com
607 394 2858

Font styles to use
Sans Serif
Decorative

Requirements
Must have
• Whatever files I need to best utilize your design
• PDF
• JPG
• EPS
• Vectorwhatsit
Nice to have
• Logo or element that can be incorporated into other print material.
• Could be a font based card
Should not have
• no clip art
• No templates
• no floor plans
• no building photographs

```html
<!DOCTYPE html>
<html lang="en">
<head>
<meta charset="utf-8">
<title>Caldwell Prusinski Architect – Business Card Options</title>
<link href="https://fonts.googleapis.com/css2?family=Roboto:wght@400;500;700;900&display=swap" rel="stylesheet">
<style>
  :root {
    --backdrop: #3b3b3b;
    --label: #ffffff;
    --brand-red: #a82121;
    --paper: #f2f2f2;
    --paper-edge: #c9c9c9;
    --ink: #111111;
    --white: #ffffff;
    --rule-light: #f0d2d2;
    --rule-red: #b4352b;
  }
  * { box-sizing: border-box; margin: 0; padding: 0; }
  html, body {
    width: 1200px; height: 933px; overflow: hidden;
    background: var(--backdrop);
    font-family: "Roboto", Arial, sans-serif;
  }
  .sheet { position: relative; width: 1200px; height: 933px; }
  .option-label {
    position: absolute; left: 219px;
    color: var(--label); font-size: 14px; font-weight: 400;
    letter-spacing: 0.2px;
  }
  .option-label--one { top: 293px; }
  .option-label--two { top: 651px; }

  .card {
    position: absolute; left: 337px; width: 525px; height: 300px;
    border-radius: 22px;
  }
  .card--red { top: 147px; background: var(--brand-red); color: var(--white); }
  .card--white { top: 485px; background: var(--paper); border: 1px solid var(--paper-edge); color: var(--ink); }

  .wordmark { position: absolute; left: 55px; top: 71px; width: 160px; height: 160px; }
  .wordmark__square { position: absolute; left: 0; top: 0; width: 20px; height: 20px; background: currentColor; }
  .wordmark__name, .wordmark__title {
    position: absolute; left: 0; font-weight: 900; text-transform: uppercase;
    line-height: 1;
  }
  .wordmark__name { top: 46px; font-size: 22px; letter-spacing: 0.5px; width: 170px; line-height: 1.05; }
  .wordmark__title { top: 127px; font-size: 19px; letter-spacing: 0.3px; }
  .card--red .wordmark { color: var(--white); }
  .card--white .wordmark { color: var(--brand-red); }
  .card--white .wordmark__title { color: var(--ink); }

  .contact { position: absolute; left: 260px; top: 76px; width: 224px; }
  .contact__name { font-size: 21px; font-weight: 700; letter-spacing: 0.2px; white-space: nowrap; }
  .card--white .contact__name { color: var(--brand-red); }
  .contact__rule { height: 1.5px; margin: 14px 0 20px; background: var(--rule-light); }
  .card--white .contact__rule { background: var(--rule-red); }
  .contact__phone { font-size: 22px; font-weight: 700; letter-spacing: 0.6px; line-height: 1; }
  .contact__email { margin-top: 8px; font-size: 17px; font-weight: 500; white-space: nowrap; }
  .contact__license { margin-top: 8px; font-size: 14px; font-weight: 700; }
</style>
</head>
<body>
<main class="sheet">
  <p class="option-label option-label--one">OPTION 1</p>
  <p class="option-label option-label--two">OPTION 2</p>

  <section class="card card--red" aria-label="Business card, red option">
    <div class="wordmark">
      <span class="wordmark__square"></span>
      <p class="wordmark__name">Caldwell<br>Prusinski</p>
      <p class="wordmark__title">Architect</p>
    </div>
    <div class="contact">
      <h1 class="contact__name">CALDWELL PRUSINSKI</h1>
      <div class="contact__rule"></div>
      <p class="contact__phone">607 394 2858</p>
      <p class="contact__email">caldwell@designcpx.com</p>
      <p class="contact__license">NY License No. 582163</p>
    </div>
  </section>

  <section class="card card--white" aria-label="Business card, white option">
    <div class="wordmark">
      <span class="wordmark__square"></span>
      <p class="wordmark__name">Caldwell<br>Prusinski</p>
      <p class="wordmark__title">Architect</p>
    </div>
    <div class="contact">
      <h2 class="contact__name">CALDWELL PRUSINSKI</h2>
      <div class="contact__rule"></div>
      <p class="contact__phone">607 394 2858</p>
      <p class="contact__email">caldwell@designcpx.com</p>
      <p class="contact__license">NY License No. 582163</p>
    </div>
  </section>
</main>
</body>
</html>
```